Pebble Grocer

Hope all is well!

Wanted to make business cards for my father. His name is Samir Haddad and owns convenience stores. I have attached logo :)

He does not want any title just simple name and phone. An email would be nice as well.

Samir Haddad
Cell: 413-555-0148
Store: 413-555-0192

Pebblegrocer518@mailnest.example

The design and style is totally up to you :) The colors we were looking for were the same as logo :)

```html
<!DOCTYPE html>
<html lang="en">
<head>
<meta charset="utf-8">
<title>Pebble Grocer — Business Card</title>
<link rel="stylesheet" href="https://fonts.googleapis.com/css2?family=Montserrat:wght@400;600;700&display=swap">
<style>
  :root {
    --navy: #223577;
    --navy-deep: #1c2c68;
    --red: #e8262f;
    --ink: #1f1f1f;
    --rule: #9a9a9a;
    --paper: #ffffff;
    --backdrop: #e9e9eb;
  }
  * { box-sizing: border-box; margin: 0; padding: 0; }
  html, body {
    width: 1200px; height: 1200px; overflow: hidden;
    background: var(--backdrop);
    font-family: "Montserrat", Arial, sans-serif;
  }
  .sheet {
    width: 1200px; height: 1200px;
    display: flex; flex-direction: column; align-items: center; justify-content: center;
    gap: 48px;
  }
  .card {
    position: relative;
    width: 900px; height: 514px;
    border-radius: 38px;
    box-shadow: 0 0 0 3px var(--red), 0 14px 30px rgba(0,0,0,.18);
    overflow: hidden;
  }
  .card--front { background: var(--paper); }
  .card--back { background: linear-gradient(135deg, var(--navy-deep), var(--navy) 55%, var(--navy-deep)); }

  .wordmark {
    position: absolute;
    font-weight: 700;
    letter-spacing: 1px;
    white-space: nowrap;
    display: flex; align-items: center; gap: 18px;
  }
  .wordmark__mark { width: 26px; height: 26px; background: var(--red); }
  .card--front .wordmark { left: 190px; top: 120px; font-size: 62px; color: var(--navy); }
  .card--back .wordmark { left: 50%; top: 50%; transform: translate(-50%, -50%); font-size: 78px; color: var(--paper); }

  .holder {
    position: absolute; left: 90px; top: 385px;
    font-size: 32px; font-weight: 600; color: var(--red);
    text-transform: uppercase; letter-spacing: .5px;
    white-space: nowrap;
  }
  .divider {
    position: absolute; left: 430px; top: 290px;
    width: 1px; height: 150px; background: var(--rule);
  }
  .contacts {
    position: absolute; left: 462px; top: 300px;
    list-style: none; display: flex; flex-direction: column; gap: 14px;
    font-size: 18px; color: var(--ink);
    white-space: nowrap;
  }
  .contacts li { display: flex; align-items: center; gap: 12px; }
  .contacts svg { width: 22px; height: 22px; flex: none; }
</style>
</head>
<body>
<main class="sheet">
  <section class="card card--front" aria-label="Card front">
    <div class="wordmark"><span class="wordmark__mark"></span>Pebble Grocer</div>
    <p class="holder">Samir Haddad</p>
    <div class="divider"></div>
    <ul class="contacts">
      <li>
        <svg viewBox="0 0 24 24" aria-hidden="true"><rect x="6" y="2" width="12" height="20" rx="2" fill="none" stroke="var(--red)" stroke-width="2"/><circle cx="12" cy="18.5" r="1.2" fill="var(--red)"/></svg>
        413-555-0148
      </li>
      <li>
        <svg viewBox="0 0 24 24" aria-hidden="true"><path d="M6.6 10.8a15 15 0 0 0 6.6 6.6l2.2-2.2c.3-.3.7-.4 1-.2 1.1.4 2.3.6 3.6.6.6 0 1 .4 1 1V20c0 .6-.4 1-1 1A17 17 0 0 1 3 4c0-.6.4-1 1-1h3.5c.6 0 1 .4 1 1 0 1.3.2 2.5.6 3.6.1.3 0 .7-.2 1z" fill="var(--red)"/></svg>
        413-555-0192
      </li>
      <li>
        <svg viewBox="0 0 24 24" aria-hidden="true"><rect x="2" y="5" width="20" height="14" rx="1.5" fill="var(--red)"/><path d="M3 6l9 7 9-7" fill="none" stroke="#fff" stroke-width="1.6"/></svg>
        Pebblegrocer518@mailnest.example
      </li>
    </ul>
  </section>

  <section class="card card--back" aria-label="Card back">
    <div class="wordmark"><span class="wordmark__mark"></span>Pebble Grocer</div>
  </section>
</main>
</body>
</html>
```